One page informative flyer for Florist

We are looking for a simple one page flyer. We are a florist who sell flowers, and commemorative t-shirts at graduation ceremonies, and need a flyer that can be given out to students so that they will know what is available on site. Further, we want the flyer to be editable (ie. a word template, or some other program), so that we can change the schools name, and change small bits of the copy easily.

What we are really looking for is a simple template, but we need 4 iterations of the flyer. With each of our two logos, I will need a flyer for t-shirts, and a flyer for flowers. Making 4 total. Please see breakdown below as explanation:

1, Tassel Lane Flowers logo - flyer for flowers
2. Tassel Lane Flowers logo - flyer for shirts
3. Brightmarch Flowers logo - flyer for flowers
4. Brightmarch Flowers logo - flyer for shirts

Please see logos for Tassel Lane Flowers and Brightmarch Flowers attached, as well as a picture of flowers and of the shirts. Feel free to use those images or stock images.

Here is the copy:

Flowers - A variety floral arrangements will be available for purchase at our stand, located conveniently at the graduation ceremony. You can browse our selection & pre-order ahead of time at: www.brightmarchflowers-example.com/index,php/test

T-Shirts - Commerative T-Shirts displaying all of the students names will be available for purchase at our stand, located conveniently at the graduation ceremony. You can pre-order ahead of time to guarantee your choice of size at: www.brightmarchflowers-example.com/index.php/test

```html
<!DOCTYPE html>
<html lang="en">
<head>
<meta charset="utf-8">
<title>Brightmarch Flowers – Graduation Flowers Flyer</title>
<link rel="stylesheet" href="https://fonts.googleapis.com/css2?family=Federo&family=Oswald:wght@500&family=Dancing+Script:wght@500&family=Great+Vibes&family=Lato:wght@400;700&display=swap">
<style>
  :root{
    --orange:#f47b2a;
    --orange-deep:#e8651c;
    --yellow:#f7e46a;
    --yellow-soft:#f9e87f;
    --green:#8cc63f;
    --green-dark:#6b9e2c;
    --green-text:#4b7d1e;
    --ink:#333333;
    --white:#ffffff;
  }
  *{margin:0;padding:0;box-sizing:border-box}
  html,body{width:865px;height:1200px;overflow:hidden;background:var(--white)}
  .flyer{position:relative;width:865px;height:1200px;overflow:hidden;background:var(--white)}

  .hero-photo{position:absolute;left:0;top:0;width:418px;height:762px;
    background:radial-gradient(circle at 45% 50%,#f6de55 0%,#e9cf3c 35%,#6d8f3a 70%,#c9b88f 100%)}

  .stripes{position:absolute;left:418px;top:0;width:447px;height:240px;
    background:repeating-linear-gradient(90deg,var(--green) 0 14px,var(--green-dark) 14px 24px)}
  .info-panel{position:absolute;left:418px;top:240px;width:447px;height:522px;
    background:var(--yellow-soft);border-top:8px solid var(--orange)}

  .school-banner{position:absolute;left:56px;top:36px;width:809px;height:80px}
  .school-name{position:absolute;left:80px;top:36px;width:785px;height:70px;
    font-family:"Federo",serif;font-size:44px;color:var(--white);
    display:flex;align-items:center;justify-content:center;padding-right:120px}

  .brand-badge{position:absolute;left:455px;top:158px;width:350px;height:136px;
    background:var(--white);border:6px solid var(--orange);border-radius:60px;
    display:flex;flex-direction:column;align-items:center;justify-content:center}
  .brand-name{font-family:"Oswald",sans-serif;font-weight:500;color:var(--green-text);
    font-size:40px;line-height:1.05;text-align:center}

  .copy{position:absolute;left:452px;top:362px;width:405px;
    font-family:"Dancing Script",cursive;font-size:31px;color:var(--green-text);line-height:1}
  .copy p{height:61px;display:flex;align-items:flex-end;white-space:nowrap}
  .copy .accent{font-family:"Great Vibes",cursive;color:var(--orange);font-size:40px;margin:0 4px}
  .copy .accent.big{font-size:54px}

  .lower{position:absolute;left:0;top:762px;width:865px;height:404px;background:var(--orange)}
  .lower-card{position:absolute;left:80px;top:762px;width:711px;height:398px;background:var(--white)}

  .bouquet{position:absolute;top:674px;width:240px;height:240px;border-radius:50%;
    background:var(--green);padding:12px}
  .bouquet .ring{width:100%;height:100%;border-radius:50%;border:4px solid var(--orange);background:var(--white);padding:5px}
  .bouquet .photo{width:100%;height:100%;border-radius:50%}
  .bouquet.pink{left:40px}
  .bouquet.white{left:287px}
  .bouquet.red{left:585px}
  .pink .photo{background:radial-gradient(circle,#f4a7b4 0%,#e98a9c 45%,#7aa04a 80%,#e8ddd0 100%)}
  .white .photo{background:radial-gradient(circle,#f7f2e2 0%,#ece4cc 45%,#7aa04a 80%,#e6ddd0 100%)}
  .red .photo{background:radial-gradient(circle,#c0202a 0%,#a51822 45%,#6f9a42 80%,#e6ddd0 100%)}

  .preorder{position:absolute;left:80px;top:932px;width:711px;text-align:center;font-family:"Lato",sans-serif}
  .preorder .lead{font-size:24px;color:var(--ink)}
  .preorder .url{font-size:33px;font-weight:700;color:var(--green-text);margin-top:6px}

  .footer-ribbon{position:absolute;left:6px;top:1034px;width:834px;height:78px}
  .partner-badge{position:absolute;left:287px;top:1020px;width:275px;height:112px;
    background:var(--white);border:5px solid var(--orange);border-radius:50%;
    display:flex;align-items:center;justify-content:center}
  .partner-badge .brand-name{font-size:36px}

  .footer-stripes{position:absolute;left:0;top:1166px;width:865px;height:34px;
    background:repeating-linear-gradient(90deg,var(--green) 0 14px,var(--green-dark) 14px 24px)}
</style>
</head>
<body>
<main class="flyer">
  <div class="hero-photo" role="img" aria-label="Photo of a bouquet of yellow roses with baby's breath"></div>
  <div class="stripes"></div>
  <div class="info-panel"></div>

  <svg class="school-banner" viewBox="0 0 809 80" aria-hidden="true">
    <polygon points="0,6 40,6 40,64 0,64 18,35" fill="var(--yellow)"/>
    <polygon points="24,3 809,3 809,66 24,66 44,34" fill="var(--orange)"/>
    <rect x="44" y="66" width="765" height="5" fill="var(--yellow)"/>
  </svg>
  <div class="school-name">School Name</div>

  <div class="brand-badge">
    <span class="brand-name">Brightmarch<br>Flowers</span>
  </div>

  <div class="copy">
    <p>A variety<span class="accent">Floral</span></p>
    <p>arrangements will be available</p>
    <p>for purchase at our<span class="accent big">Stand</span>,</p>
    <p>located conveniently at the</p>
    <p><span class="accent">Graduation Ceremony</span>.</p>
  </div>

  <div class="lower"></div>
  <div class="lower-card"></div>

  <div class="bouquet pink"><div class="ring"><div class="photo" role="img" aria-label="Photo of a pink rose bouquet"></div></div></div>
  <div class="bouquet white"><div class="ring"><div class="photo" role="img" aria-label="Photo of a white rose bouquet"></div></div></div>
  <div class="bouquet red"><div class="ring"><div class="photo" role="img" aria-label="Photo of a red rose bouquet"></div></div></div>

  <div class="preorder">
    <p class="lead">You can browse our selection &amp; pre-order ahead of time at:</p>
    <p class="url">www.brightmarchflowers-example.com</p>
  </div>

  <svg class="footer-ribbon" viewBox="0 0 834 78" aria-hidden="true">
    <polygon points="0,10 834,10 808,40 834,70 0,70 26,40" fill="var(--yellow)"/>
    <rect x="30" y="26" width="774" height="18" fill="var(--green)"/>
  </svg>
  <div class="partner-badge">
    <span class="brand-name">Tassel Lane<br>Flowers</span>
  </div>

  <div class="footer-stripes"></div>
</main>
</body>
</html>
```